VantoMedix website

I have a plumfield hosting website already & have been using wordpress.
See www.vantomedix-sample.com
I have a logo's already.
I need a front page "VantoMedix". I have 3 products: (need separate pages)
1) the "GlideTray" (can't supply images ATM)
2) the "TubeKeeper" (several stills below & animation: http://www.clipvault-example.com/watch?v=Z7HqR20mW3x&list=QPtr8B_kzoepWnXcM4Lq5B_T&feature=share)
3) the "FastPart" animation here: http://clipv.example/pwrtk-Mmo_E & logo as below

It needs to be corporate & professional looking. VantoMedix is an innovative design house for medical devices.

Reason: Hi Designers, thanks for all your work to date - there have been some great designs. We'll be providing feedback to some of you in the near future. The reason we have extended the deadline is simply that we are too busy with other aspects of the business to focus on this at the moment. Kind regards, the VantoMedix team.

Dear Designers,

VantoMedix apologies for the delay due to our busyness. 
Please help us to understand the process here:
are we getting fully working websites? With multiple pages? Will we be able to modify them?
If not, what is the output?

Kind regards,
the Vanto team.

```html
<!DOCTYPE html>
<html lang="en">
<head>
<meta charset="utf-8">
<title>VantoMedix</title>
<link href="https://fonts.googleapis.com/css2?family=Open+Sans:wght@400;600;700&display=swap" rel="stylesheet">
<style>
:root{
  --blue:#1f9ad8;
  --band:#3aade2;
  --band-dark:#2192d2;
  --orange:#f26a10;
  --label:#f05a0a;
  --text:#4a4a4a;
  --muted:#6b6b6b;
  --footer:#3e3e3e;
  --line:#d6d6d6;
  --white:#ffffff;
}
*{margin:0;padding:0;box-sizing:border-box}
html,body{width:964px;height:1200px;overflow:hidden;background:var(--white);font-family:"Open Sans",Arial,sans-serif;color:var(--text)}
.page{position:relative;width:964px;height:1200px}
.abs{position:absolute}

.brand{left:105px;top:22px;display:flex;align-items:center;gap:6px;font-size:27px;font-weight:700;color:var(--blue);letter-spacing:-0.5px}
.brand-dot{width:16px;height:16px;border-radius:50%;background:var(--orange)}
.nav{top:32px;left:366px;font-size:13px;color:#555}
.nav a{color:inherit;text-decoration:none;position:absolute;white-space:nowrap}
.nav .active{color:var(--blue)}
.search{left:710px;top:31px;width:148px;height:22px;border:1px solid #d9d9d9;border-radius:2px;font-size:9px;color:#aaa;padding:5px 8px}
.search svg{position:absolute;right:4px;top:5px}

.hero{left:0;top:81px;width:964px;height:354px;background:radial-gradient(ellipse at 40% 45%,#3fb2ff 0%,#0a78d6 45%,#063f86 100%)}
.hero-caption{left:474px;top:195px;width:386px;height:127px;background:rgba(25,40,60,.82);color:#fff;font-size:18px;line-height:36px;text-align:center;padding-top:26px}
.arrow{width:28px;height:28px;top:244px}

.h2{font-size:24px;font-weight:700;color:var(--orange)}
.facts{left:105px;top:494px;width:420px;font-size:9.8px;line-height:21px;color:var(--text);white-space:nowrap;letter-spacing:-0.05px}
.facts p+p{margin-top:18px}
.chart{left:533px;top:463px;width:326px;height:194px;border:1px solid var(--line);background:#fff}

.card{top:740px;width:234px;height:251px;border:1px solid #d8d8d8;background:#f3f3f3;box-shadow:0 1px 2px rgba(0,0,0,.12)}
.card-media{position:absolute;left:0;top:0;width:100%;height:165px}
.play{position:absolute;left:100px;top:65px}
.card-label{position:absolute;left:35px;top:144px;width:163px;height:34px;background:var(--label);padding:4px 7px}
.card-label span{display:block;height:100%;border:1px solid rgba(255,255,255,.85);color:#fff;font-size:12px;font-weight:600;text-align:center;line-height:24px;letter-spacing:.3px}
.card-text{position:absolute;left:0;top:195px;width:100%;text-align:center;font-size:10px;line-height:19px;color:var(--muted)}

.band{left:0;top:1058px;width:964px;height:60px;background:var(--band)}
.envelope{left:85px;top:1066px;width:85px;height:52px;background:var(--band-dark)}
.band-text{left:206px;top:1080px;width:532px;font-size:11.8px;font-weight:600;color:#fff;white-space:nowrap}
.signup{left:778px;top:1079px;width:79px;height:23px;background:#fff;color:var(--band);font-size:11px;font-weight:700;text-align:center;line-height:23px}

.footer{left:0;top:1118px;width:964px;height:82px;background:var(--footer);color:#fff;font-size:10px}
.footer-links{left:105px;top:22px}
.footer-copy{left:103px;top:48px}
.product-tag{top:33px;height:17px;background:#fff;color:#1f2a44;font-size:9.5px;font-weight:700;text-align:center;line-height:17px;letter-spacing:.5px}
.social{top:31px;width:20px;height:20px;border-radius:50%;border:2px solid #cfd6de}
</style>
</head>
<body>
<div class="page">

  <header>
    <div class="abs brand"><span>VantoMedix</span><span class="brand-dot"></span></div>
    <nav class="abs nav">
      <a class="active" style="left:0">Home</a>
      <a style="left:68px">About</a>
      <a style="left:132px">Ask a Question</a>
      <a style="left:248px">Contact Us</a>
    </nav>
    <div class="abs search">Enter ant keyword
      <svg width="10" height="10" viewBox="0 0 10 10"><circle cx="6" cy="4" r="3" fill="none" stroke="#e8742c" stroke-width="1.4"/><line x1="4" y1="6" x2="1" y2="9" stroke="#e8742c" stroke-width="1.6"/></svg>
    </div>
  </header>

  <section class="abs hero" role="img" aria-label="Glowing blue x-ray style illustration of a runner with an injured knee"></section>
  <div class="abs hero-caption">Neque porro quisquam est qui dolorem<br>ipsum quia dolor sit amet, consectetur,</div>
  <svg class="abs arrow" style="left:21px" viewBox="0 0 28 28"><circle cx="14" cy="14" r="14" fill="#fff"/><polyline points="16,7 9,14 16,21" fill="none" stroke="#0a4f9c" stroke-width="3.5"/></svg>
  <svg class="abs arrow" style="left:910px" viewBox="0 0 28 28"><circle cx="14" cy="14" r="14" fill="#fff"/><polyline points="12,7 19,14 12,21" fill="none" stroke="#0a4f9c" stroke-width="3.5"/></svg>

  <h2 class="abs h2" style="left:103px;top:454px">Did you know?</h2>
  <div class="abs facts">
    <p>The cost of paramedic (EMS) injury in Australia is over $32,000 dollars a day?<br>
    (That translates to well over half a billion dollars every year globally.)<br>
    17% of injured paramedics remain off duty for over a month?<br>
    Two thirds of injuries to paramedics affect the back and come from lifting &amp; carrying?</p>
    <p>VantoMedix has created a fully integrated system to help paramedics remove patients<br>
    from everyday awkward situations:&nbsp; down stairs, around tight corners &amp; out of small rooms.<br>
    All with a minimum of lifting and carrying.</p>
  </div>

  <svg class="abs chart" viewBox="0 0 326 194" font-family="Open Sans, Arial, sans-serif">
    <g stroke="#e2e2e2" stroke-width="1">
      <line x1="28" y1="154" x2="307" y2="154"/><line x1="28" y1="136.5" x2="307" y2="136.5"/>
      <line x1="28" y1="119" x2="307" y2="119"/><line x1="28" y1="101.5" x2="307" y2="101.5"/>
      <line x1="28" y1="84" x2="307" y2="84"/><line x1="28" y1="66.5" x2="307" y2="66.5"/>
      <line x1="28" y1="49" x2="307" y2="49"/><line x1="28" y1="31.5" x2="307" y2="31.5"/>
      <line x1="28" y1="14" x2="307" y2="14"/>
    </g>
    <g font-size="7.5" fill="#555" text-anchor="end">
      <text x="20" y="157">0</text><text x="20" y="139.5">5</text><text x="20" y="122">10</text>
      <text x="20" y="104.5">15</text><text x="20" y="87">20</text><text x="20" y="69.5">25</text>
      <text x="20" y="52">30</text><text x="20" y="34.5">35</text><text x="20" y="17">40</text>
    </g>
    <text x="165" y="29" font-size="7.5" font-weight="700" fill="#222" text-anchor="middle">Occupational Injury Rates per 100 FT workers per year</text>
    <rect x="49" y="43" width="72" height="78" fill="#2f5f8c" role="img" aria-label="Illustration of a person holding a painful lower back"/>
    <g fill="#5b9bd5">
      <rect x="47" y="133" width="18" height="21"/>
      <rect x="103" y="129.5" width="18" height="24.5"/>
      <rect x="158" y="105" width="18" height="49"/>
      <rect x="214" y="91" width="18" height="63"/>
    </g>
    <rect x="270" y="31.5" width="18" height="122.5" fill="#ffc000"/>
    <g font-size="7.5" fill="#555" text-anchor="middle">
      <text x="56" y="167">National</text><text x="56" y="177">average</text>
      <text x="112" y="167">Health workers</text>
      <text x="167" y="167">Police</text>
      <text x="223" y="167">Fire</text>
      <text x="279" y="167">EMS</text>
    </g>
  </svg>

  <h2 class="abs h2" style="left:106px;top:688px">Services</h2>

  <article class="abs card" style="left:105px">
    <div class="card-media" role="img" aria-label="3D render of the GlideTray board with straps and handles" style="background:linear-gradient(160deg,#55565a 0%,#a9a9c4 35%,#c9c9e2 100%)"></div>
    <svg class="play" width="34" height="34" viewBox="0 0 34 34"><circle cx="17" cy="17" r="16" fill="rgba(70,70,80,.55)" stroke="#fff" stroke-width="1.5"/><polygon points="13,10 25,17 13,24" fill="#fff"/></svg>
    <div class="card-label"><span>GLIDETRAY</span></div>
    <p class="card-text">Neque porro quisquam est qui dolorem ipsum<br>quia dolor sit amet, consectetur, adipisci velit</p>
  </article>

  <article class="abs card" style="left:365px">
    <div class="card-media" role="img" aria-label="3D render of the TubeKeeper wrist cuff on a hand" style="background:linear-gradient(170deg,#e6e6ec 0%,#b9b9dc 50%,#d9d2cc 100%)"></div>
    <svg class="play" width="34" height="34" viewBox="0 0 34 34"><circle cx="17" cy="17" r="16" fill="rgba(70,70,80,.45)" stroke="#fff" stroke-width="1.5"/><polygon points="13,10 25,17 13,24" fill="#fff"/></svg>
    <div class="card-label"><span>TUBEKEEPER</span></div>
    <p class="card-text">Neque porro quisquam est qui dolorem ipsum<br>quia dolor sit amet, consectetur, adipisci velit</p>
  </article>

  <article class="abs card" style="left:624px">
    <div class="card-media" role="img" aria-label="3D render of the FastPart device in use in a vehicle seat" style="background:linear-gradient(90deg,#b01818 0%,#6d5a55 35%,#7a3a40 65%,#b51a1a 100%)"></div>
    <svg class="play" width="34" height="34" viewBox="0 0 34 34"><circle cx="17" cy="17" r="16" fill="rgba(70,70,80,.45)" stroke="#fff" stroke-width="1.5"/><polygon points="13,10 25,17 13,24" fill="#fff"/></svg>
    <div class="card-label"><span>FASTPART</span></div>
    <p class="card-text">Neque porro quisquam est qui dolorem ipsum<br>quia dolor sit amet, consectetur, adipisci velit</p>
  </article>

  <section class="abs band"></section>
  <div class="abs envelope" role="img" aria-label="Blue envelope illustration for the newsletter"></div>
  <div class="abs band-text">Neque porro quisquam est qui dolorem ipsum quia dolor sit amet, consectetur, adipisci velit</div>
  <div class="abs signup">SIGN UP</div>

  <footer class="abs footer">
    <div class="abs footer-links">Home&nbsp; | &nbsp;About &nbsp; | &nbsp;Ask a question&nbsp; | &nbsp;Contact Us.</div>
    <div class="abs footer-copy">all copyrights are reserved</div>
    <div class="abs product-tag" style="left:524px;width:93px">TUBEKEEPER IV</div>
    <div class="abs product-tag" style="left:623px;width:95px">FASTPART</div>
    <div class="abs social" style="left:727px;background:#c9302c"></div>
    <div class="abs social" style="left:750px;background:#2a9fd8"></div>
    <div class="abs social" style="left:773px;background:#3b5998"></div>
    <div class="abs social" style="left:796px;background:#d34836"></div>
    <div class="abs social" style="left:819px;background:#f26a22"></div>
    <div class="abs social" style="left:842px;background:#0e76a8"></div>
  </footer>

</div>
</body>
</html>
```